Harriet Voss Consortium - Paediatric Lower Limb Surgery Agenda Forming Collective

A 2-sided A4 leaflet to explain the research priorities in Children's Orthopaedic Surgery.
We would like this to be similar to that produced previously by the physiotherapists.

```html
<!DOCTYPE html>
<html lang="en">
<head>
<meta charset="utf-8">
<title>Our top-10 research priorities</title>
<link rel="stylesheet" href="https://fonts.googleapis.com/css2?family=Montserrat:wght@600;700;800&family=Nunito:wght@900&display=swap">
<style>
  :root{
    --orange:#f6ad1e;
    --lime:#d6d623;
    --sage:#a0c9bb;
    --teal:#0d92a2;
    --teal-text:#0f8f9f;
    --navy:#2a2278;
    --red:#e3202b;
    --white:#ffffff;
  }
  *{margin:0;padding:0;box-sizing:border-box}
  html,body{width:848px;height:1200px;overflow:hidden;background:var(--white)}
  .leaflet{position:relative;width:848px;height:1200px;font-family:"Montserrat",Arial,sans-serif}
  .leaflet__title{position:absolute;top:30px;left:0;width:848px;text-align:center;font-size:29px;font-weight:800;color:var(--teal-text);letter-spacing:-0.2px}
  .panels{position:absolute;top:0;left:0}
  .panel-number{font-family:"Nunito",Arial,sans-serif;font-weight:900;font-size:84px}
  .priority{position:absolute;font-size:15px;font-weight:700;line-height:18.4px;letter-spacing:0.4px;white-space:nowrap}
  .priority--light{color:var(--white)}
  .priority--teal{color:var(--teal-text)}
  .thanks{position:absolute;left:46px;top:1012px;font-size:19.5px;font-weight:800;color:var(--navy);line-height:24px}
  .partner{position:absolute;display:flex;align-items:center;gap:7px;font-size:12px;font-weight:700;color:var(--navy);line-height:14px}
  .partner__mark{width:16px;height:16px;flex:none}
  .partner__mark--circle{border-radius:50%;background:var(--navy)}
  .partner__mark--square{background:var(--red)}
  .partner--pill{color:var(--red)}
  .credits{position:absolute;left:377px;top:1084px}
  .credits__heading{font-size:17px;font-weight:800;color:var(--teal-text);margin-bottom:6px}
  .credits__list{list-style:none;font-size:13.2px;font-weight:700;color:var(--navy);line-height:16px;white-space:nowrap}
</style>
</head>
<body>
<main class="leaflet">
  <h1 class="leaflet__title">Our top-10 research priorities</h1>

  <svg class="panels" width="848" height="1200" viewBox="0 0 848 1200" aria-hidden="true">
    <defs>
      <path id="blob-left" d="M0,0 H86 C100,0 104,8 108,16 C114,28 132,26 132,41 C132,56 112,54 106,62 C100,72 96,82 82,82 H0 Z"/>
      <path id="blob-right" d="M0,0 H-86 C-100,0 -104,-8 -108,-16 C-114,-28 -132,-26 -132,-41 C-132,-56 -112,-54 -106,-62 C-100,-72 -96,-82 -82,-82 H0 Z"/>
      <path id="blob-right-wide" d="M0,0 H-116 C-130,0 -134,-8 -138,-16 C-144,-28 -158,-26 -158,-41 C-158,-56 -142,-54 -136,-62 C-130,-72 -126,-82 -112,-82 H0 Z"/>
    </defs>

    <polygon points="10,72 462,72 384,230 10,230" fill="var(--orange)"/>
    <use href="#blob-left" x="10" y="72" fill="var(--white)"/>
    <text class="panel-number" x="28" y="146" fill="var(--orange)">1</text>
    <polygon points="462,94 836,94 836,252 384,252" fill="var(--lime)"/>
    <use href="#blob-right" x="836" y="252" fill="var(--white)"/>
    <text class="panel-number" x="822" y="242" text-anchor="end" fill="var(--lime)">2</text>

    <polygon points="10,262 462,262 384,420 10,420" fill="var(--sage)"/>
    <use href="#blob-left" x="10" y="262" fill="var(--white)"/>
    <text class="panel-number" x="26" y="330" fill="var(--sage)">3</text>
    <polygon points="462,284 836,284 836,442 384,442" fill="var(--teal)"/>
    <use href="#blob-right" x="836" y="442" fill="var(--white)"/>
    <text class="panel-number" x="824" y="426" text-anchor="end" fill="var(--teal)">4</text>

    <polygon points="10,452 462,452 384,610 10,610" fill="var(--lime)"/>
    <use href="#blob-left" x="10" y="452" fill="var(--white)"/>
    <text class="panel-number" x="28" y="520" fill="var(--lime)">5</text>
    <polygon points="462,474 836,474 836,632 384,632" fill="var(--orange)"/>
    <use href="#blob-right" x="836" y="632" fill="var(--white)"/>
    <text class="panel-number" x="822" y="622" text-anchor="end" fill="var(--orange)">6</text>

    <polygon points="10,642 462,642 384,800 10,800" fill="var(--teal)"/>
    <use href="#blob-left" x="10" y="642" fill="var(--white)"/>
    <text class="panel-number" x="28" y="708" fill="var(--teal)">7</text>
    <polygon points="462,664 836,664 836,822 384,822" fill="var(--sage)"/>
    <use href="#blob-right" x="836" y="822" fill="var(--white)"/>
    <text class="panel-number" x="822" y="808" text-anchor="end" fill="var(--sage)">8</text>

    <polygon points="10,832 462,832 384,990 10,990" fill="var(--lime)"/>
    <use href="#blob-left" x="10" y="832" fill="var(--white)"/>
    <text class="panel-number" x="24" y="894" fill="var(--lime)">9</text>
    <polygon points="462,854 836,854 836,1008 384,1008" fill="var(--orange)"/>
    <use href="#blob-right-wide" x="836" y="1008" fill="var(--white)"/>
    <text class="panel-number" x="828" y="986" text-anchor="end" fill="var(--orange)">10</text>
  </svg>

  <p class="priority priority--light" style="left:162px;top:90px">What are the best ways to<br>measure the outcome<br>following lower limb<br>orthopaedic surgery in<br>children?</p>
  <p class="priority priority--teal" style="left:468px;top:109px">Following orthopaedic<br>surgery to the lower limbs,<br>what should children's<br>rehabilitation include, how<br>long is it expected to last<br>and how does it affect the<br>result of treatment?</p>

  <p class="priority priority--teal" style="left:147px;top:274px">What is the short-term and<br>long-term clinical and cost<br>effectiveness of orthopaedic<br>lower limb surgery (including<br>best timing and technique) for<br>children with Cerebral Palsy<br>who can walk?</p>
  <p class="priority priority--light" style="left:463px;top:311px">What are the short term and<br>long term outcomes of surgery<br>compared to non-surgical care<br>in the treatment of Perthes<br>disease of the hip?</p>

  <p class="priority priority--teal" style="left:150px;top:473px">What is the clinical and cost<br>effectiveness of pre-operative<br>rehabilitation in children<br>presenting with lower limb<br>orthopaedic conditions?</p>
  <p class="priority priority--light" style="left:470px;top:492px">What is the short-term and<br>long-term clinical and cost<br>effectiveness of Selective<br>Dorsal Rhizotomy (SDR) in<br>children with Cerebral<br>Palsy who can walk?</p>

  <p class="priority priority--light" style="left:146px;top:641px">Can surveillance and non-surgical<br>treatment (e.g. physiotherapy,<br>botulinum toxin injections,<br>functional electrical stimulation,<br>orthotics, casting) prevent the<br>development of deformity<br>requiring surgery in children<br>with Cerebral Palsy?</p>
  <p class="priority priority--teal" style="left:463px;top:685px">What is the best method of<br>screening for Developmental<br>Dysplasia of the Hip (DDH) in<br>terms of clinical and cost<br>effectiveness?</p>

  <p class="priority priority--teal" style="left:149px;top:842px">What are the best strategies<br>to optimise communication<br>of information between<br>patients/carers and<br>clinicians in order to enable<br>shared decision-making?</p>
  <p class="priority priority--light" style="left:466px;top:889px">What is the best<br>management for hip<br>displacement in<br>children with Cerebral<br>Palsy?</p>

  <p class="thanks">Many thanks to all those people who helped us take this work<br>off the ground and helped us finish it!</p>

  <div class="partner" style="left:40px;top:1120px;width:110px">
    <span class="partner__mark partner__mark--circle"></span>
    <span>Allied Bone &amp; Joint Guild</span>
  </div>
  <div class="partner partner--pill" style="left:160px;top:1120px;width:200px">
    <span class="partner__mark partner__mark--square"></span>
    <span>NSYLS Northbridge Society for Young Limb Surgery</span>
  </div>

  <section class="credits">
    <h2 class="credits__heading">Special thanks to:</h2>
    <ul class="credits__list">
      <li>The Northbridge Society for Young Limb Surgery</li>
      <li>The Allied Bone &amp; Joint Guild</li>
      <li>The University of Elmstead and the</li>
      <li>Harriet Voss Consortium, who always look for fair play in research!</li>
    </ul>
  </section>
</main>
</body>
</html>
```